Hip and quirky Indian restaurant Menu

We need a build your own bowl/meal/wrap menu similar to Verdigo others. We would like illustrations if possible of India/veggies/chicken/animals/themes. Please utilize the colors that match the schema of the logos provided. We have included pictures you may use them if you would like to. Menu provided is our old menu.

Target Market(s)

Millenials, Ge

Industry/Entity Type

Retail

Font styles to use
Sans Serif
Decorative

Requirements
Must have
• logical placements for build your own meal options
Nice to have
• Illustrations.

```html
<!DOCTYPE html>
<html lang="en">
<head>
<meta charset="utf-8">
<title>Masala Lane – Menu</title>
<link href="https://fonts.googleapis.com/css2?family=Oswald:wght@500;600&family=Montserrat:wght@400;500;700&display=swap" rel="stylesheet">
<style>
  :root {
    --page: #e9e7e4;
    --paper: #ffffff;
    --orange: #ee7a4e;
    --blue: #4b55a1;
    --magenta: #a63a7c;
    --red: #e43b4f;
    --navy: #3e3a7a;
    --yellow: #f2ba4b;
    --cream: #f8dcaa;
    --plum: #a2307b;
    --white: #ffffff;
  }
  * { margin: 0; padding: 0; box-sizing: border-box; }
  html, body { width: 1200px; height: 900px; overflow: hidden; }
  body { background: var(--page); font-family: "Montserrat", sans-serif; position: relative; }

  .menu {
    position: absolute; left: 15px; top: 57px; width: 1170px; height: 786px;
    background: var(--paper); overflow: hidden;
    box-shadow: 0 2px 6px rgba(0,0,0,.12);
  }
  .pattern {
    position: absolute; inset: 0;
    background:
      radial-gradient(circle at 30% 62%, rgba(248,220,170,.55) 0 14%, rgba(248,220,170,0) 38%),
      radial-gradient(circle at 70% 30%, rgba(248,220,170,.45) 0 10%, rgba(248,220,170,0) 34%),
      radial-gradient(circle at 60% 85%, rgba(248,220,170,.45) 0 8%, rgba(248,220,170,0) 30%);
  }

  .rough {
    position: absolute;
    clip-path: polygon(2% 3%, 8% 0, 20% 2%, 33% 0, 47% 3%, 60% 0, 74% 2%, 88% 0, 98% 3%, 100% 12%, 98% 25%, 100% 40%, 98% 55%, 100% 70%, 98% 85%, 100% 96%, 90% 100%, 76% 97%, 62% 100%, 48% 97%, 34% 100%, 20% 97%, 8% 100%, 0 95%, 2% 80%, 0 65%, 2% 50%, 0 35%, 2% 20%, 0 8%);
  }
  .splash {
    clip-path: polygon(8% 18%, 20% 14%, 30% 4%, 42% 8%, 50% 0, 60% 10%, 74% 6%, 84% 16%, 96% 20%, 100% 38%, 96% 52%, 100% 68%, 94% 82%, 82% 86%, 70% 98%, 58% 92%, 48% 100%, 36% 90%, 22% 94%, 12% 84%, 0 76%, 4% 60%, 0 44%, 4% 28%);
  }

  .logo-block { left: 27px; top: 0; width: 304px; height: 260px; background: var(--orange);
    display: flex; flex-direction: column; justify-content: center; align-items: center; gap: 14px; }
  .logo-name { font-family: "Oswald", sans-serif; font-weight: 600; color: var(--white);
    font-size: 52px; line-height: .95; text-transform: uppercase; text-align: center; }
  .logo-dot { width: 14px; height: 14px; border-radius: 50%; background: var(--white); }

  .build { position: absolute; left: 27px; width: 304px; top: 274px; text-align: center; }
  .build-title { font-family: "Oswald", sans-serif; font-weight: 600; font-size: 44px; line-height: 1.05; text-transform: uppercase; }
  .build-title .line-1 { color: var(--orange); display: block; }
  .build-title .line-2 { color: var(--plum); display: block; }
  .price-tag { display: inline-block; margin-top: 6px; background: var(--orange); color: var(--white);
    font-family: "Oswald", sans-serif; font-size: 15px; padding: 1px 8px; border-radius: 3px; }

  .step { position: absolute; left: 27px; width: 304px; text-align: center; }
  .step-label { font-weight: 700; font-size: 14px; text-transform: uppercase; }
  .brush { margin: 6px auto 0; width: 295px; padding: 8px 24px; color: var(--white); font-size: 11px; line-height: 1.35;
    clip-path: polygon(3% 20%, 14% 6%, 30% 12%, 50% 0, 72% 10%, 90% 2%, 100% 14%, 94% 40%, 100% 62%, 96% 88%, 80% 96%, 60% 88%, 40% 100%, 20% 90%, 4% 96%, 0 72%, 4% 50%, 0 34%); }
  .step-bowl { top: 420px; } .step-bowl .step-label { color: var(--plum); } .step-bowl .brush { background: var(--magenta); }
  .step-curry { top: 513px; } .step-curry .step-label { color: var(--red); } .step-curry .brush { background: var(--red); }
  .step-toppings { top: 606px; } .step-toppings .step-label { color: var(--navy); } .step-toppings .brush { background: var(--navy); }
  .step-sauces { top: 698px; } .step-sauces .step-label { color: var(--yellow); } .step-sauces .brush { background: var(--yellow); }

  .section-title { font-family: "Oswald", sans-serif; font-weight: 500; font-variant: small-caps; color: var(--white);
    font-size: 27px; line-height: 1.05; text-align: center; letter-spacing: .5px; }

  .lassi-block { left: 391px; top: 0; width: 322px; height: 243px; background: var(--orange); padding: 22px 36px 0; }
  .lassi-table { width: 100%; margin-top: 10px; border-collapse: collapse; color: var(--white); font-size: 11px; }
  .lassi-table th { font-size: 6px; font-weight: 700; text-align: left; padding-bottom: 5px; }
  .lassi-table td { padding: 1px 0; }
  .lassi-table .col-price { width: 48px; }

  .food-photos { position: absolute; left: 756px; top: 12px; width: 353px; height: 341px;
    background: radial-gradient(circle at 30% 25%, #c9a27a, #8a6a4f 40%, rgba(240,236,230,0) 72%),
                radial-gradient(circle at 60% 75%, #d9b06a, #7d5c3e 40%, rgba(240,236,230,0) 70%);
    border-radius: 40% 50% 45% 55%; }

  .biryani-block { position: absolute; left: 403px; top: 272px; width: 336px; height: 238px; background: var(--blue);
    padding: 70px 30px 0; text-align: center; }
  .block-copy { color: var(--white); font-size: 10.5px; line-height: 1.35; margin-top: 10px; }

  .snacks-block { position: absolute; left: 403px; top: 515px; width: 336px; height: 238px; background: var(--magenta);
    padding: 60px 42px 0; }
  .price-list { list-style: none; color: var(--white); font-size: 11px; margin-top: 8px; }
  .price-list li { display: flex; justify-content: space-between; line-height: 1.3; }

  .right-column { left: 791px; top: 353px; width: 321px; height: 433px; background: var(--orange);
    padding: 48px 20px 0; text-align: center; }
  .right-column .section-title + .item-list { margin-bottom: 18px; }
  .item-list { list-style: none; color: var(--white); font-size: 11px; line-height: 1.3; margin-top: 6px; }
</style>
</head>
<body>
  <main class="menu">
    <div class="pattern" role="img" aria-label="Faint cream mandala pattern across the menu background"></div>

    <header class="logo-block rough">
      <div class="logo-dot"></div>
      <h1 class="logo-name">Masala<br>Lane</h1>
    </header>

    <section class="build">
      <h2 class="build-title"><span class="line-1">Build Your</span><span class="line-2">Own Meal</span></h2>
      <span class="price-tag">$8.00</span>
    </section>

    <div class="step step-bowl">
      <p class="step-label">Pick Bowl/Wrap</p>
      <p class="brush">Salad Bowl, Basmati Rice Bowl,<br>Curry Rice Bowl, Paratha Wrap</p>
    </div>
    <div class="step step-curry">
      <p class="step-label">Pick Main Curry Option</p>
      <p class="brush">Veg Korma, Chana Masala, CTM,<br>Chili Chicken, Tandoori Chicken,<br>Beef Curry +$1, Goat Curry $2</p>
    </div>
    <div class="step step-toppings">
      <p class="step-label">Pick Toppings</p>
      <p class="brush">Beets Thoran, Green Beans Thoran,<br>Cabbage Thoran, Chick Pea Salad<br>Cucumber Salad, diced Onion</p>
    </div>
    <div class="step step-sauces">
      <p class="step-label">Pick Sauces</p>
      <p class="brush">Original Mint, Sweet Tamarind,<br>Cool Yogurt, Mango Chilli, Tikka Masala</p>
    </div>

    <section class="lassi-block rough">
      <h2 class="section-title">Lassi/<br>Indian Shakes</h2>
      <table class="lassi-table">
        <thead><tr><th></th><th class="col-price">SMALL</th><th class="col-price">LARGE</th></tr></thead>
        <tbody>
          <tr><td>Original Lassi</td><td>2.00</td><td>2.50</td></tr>
          <tr><td>Mango Lassi</td><td>2.5</td><td>3.00</td></tr>
          <tr><td>Rose Lassi</td><td>2.5</td><td>3.00</td></tr>
          <tr><td>Chai Spice Lassi</td><td>2.75</td><td>3.25</td></tr>
          <tr><td>Cookies N Cream Lassi</td><td>2.75</td><td>3.25</td></tr>
          <tr><td>Chocolate Hazelnut Lassi</td><td>2.75</td><td>3.25</td></tr>
        </tbody>
      </table>
    </section>

    <div class="food-photos" role="img" aria-label="Photos of curry bowls, biryani and side dishes"></div>

    <section class="biryani-block splash">
      <h2 class="section-title">Chicken<br>Biriyani Bowl</h2>
      <p class="block-copy">The Original Indian Rice Bowl! Chicken and rice which has been baked to perfection." Served with yogurt sauce, pickle and pappadom.</p>
    </section>

    <section class="snacks-block splash">
      <h2 class="section-title">Snacks</h2>
      <ul class="price-list">
        <li><span>Samosa</span><span>$1.00</span></li>
        <li><span>Veg Puffs</span><span>$1.49</span></li>
        <li><span>Egg Puffs</span><span>$2.49</span></li>
        <li><span>Sweet Puffs</span><span>$1.49</span></li>
        <li><span>Beef Puffs</span><span>$1.49</span></li>
        <li><span>Chicken Puffs</span><span>$1.49</span></li>
      </ul>
    </section>

    <section class="right-column rough">
      <h2 class="section-title">Chicken<br>Meals</h2>
      <ul class="item-list">
        <li>Tandoori Chicken /Fries $7</li>
        <li>Chicken Tender/ Fries $7</li>
        <li>Spicy Chicken Tender/ Fries $7</li>
      </ul>
      <h2 class="section-title">Loaded<br>Fries</h2>
      <ul class="item-list">
        <li>Chicken Tikka Fries</li>
        <li>Tandoori Fries</li>
        <li>Chili Chicken Fries</li>
      </ul>
      <h2 class="section-title" style="margin-top:18px">Drinks</h2>
      <ul class="item-list">
        <li>Iced Tea 32oz</li>
        <li>Lemonade 32oz</li>
        <li>Masala Tea</li>
        <li>Indian Coffee</li>
        <li>Soda Can</li>
        <li>Water Bottle</li>
      </ul>
    </section>
  </main>
</body>
</html>
```